Advertisement Design

I'm looking for a post card sized advertisement piece that I will be dropping off to commercial and residential customers.
On one side I want it promoting carpet cleaning services and on the other side dryer vent cleaning services.
I've uploaded two different layouts of my company logo for you to choice from.
One batch will be printed with my Michigan Number
One batch will be printed with my Tennessee number
Will share contact numbers with the winner so just use a make up number
555-319-4826

Slow in providing feedback

```html
<!DOCTYPE html>
<html lang="en">
<head>
<meta charset="utf-8">
<title>Fiber Nest Postcards</title>
<link href="https://fonts.googleapis.com/css2?family=Montserrat:wght@500;600;700&display=swap" rel="stylesheet">
<style>
  :root {
    --stage: #000000;
    --paper: #ffffff;
    --brand-blue: #0a80c6;
    --slate: #58585a;
    --ink: #464646;
    --body-ink: #1a1a1a;
    --rule: #bdbdbd;
  }
  * { margin: 0; padding: 0; box-sizing: border-box; }
  html, body { width: 675px; height: 1200px; overflow: hidden; background: var(--stage); }
  body { position: relative; font-family: "Montserrat", Arial, sans-serif; }

  .postcard {
    position: absolute;
    left: 67px;
    width: 539px;
    height: 359px;
    background: var(--paper);
    overflow: hidden;
  }
  .postcard--carpet { top: 185px; }
  .postcard--vent { top: 656px; }

  .postcard__art { position: absolute; inset: 0; width: 539px; height: 359px; }

  .brand {
    position: absolute;
    left: 17px;
    top: 24px;
    height: 26px;
    display: flex;
    align-items: center;
  }
  .brand__mark { width: 22px; height: 22px; background: var(--brand-blue); }
  .brand__rule { width: 1px; height: 40px; background: var(--ink); margin: 0 6px 0 7px; }
  .brand__name { color: var(--brand-blue); font-weight: 600; font-size: 11px; letter-spacing: 0.5px; }

  .audience {
    position: absolute;
    left: 11px;
    top: 70px;
    color: var(--paper);
    font-weight: 600;
    font-size: 10.6px;
    line-height: 21px;
  }

  .headline {
    position: absolute;
    left: 17px;
    font-weight: 700;
    text-transform: uppercase;
    color: var(--ink);
  }
  .headline span { display: block; }
  .headline .accent { color: var(--brand-blue); }
  .postcard--carpet .headline { top: 99px; font-size: 40px; line-height: 33px; }
  .postcard--vent .headline { top: 110px; }
  .postcard--vent .headline .lead { font-size: 18.5px; line-height: 22px; letter-spacing: 0.3px; }
  .postcard--vent .headline .big { font-size: 35px; line-height: 36px; }

  .blurb {
    position: absolute;
    left: 17px;
    top: 206px;
    width: 230px;
    color: var(--body-ink);
    font-weight: 700;
    font-size: 8.9px;
    line-height: 11.5px;
  }
  .postcard--vent .blurb { top: 210px; }

  .hours {
    position: absolute;
    left: 17px;
    top: 320px;
    color: var(--paper);
    font-weight: 500;
    font-size: 11px;
    line-height: 14px;
  }

  .phone {
    position: absolute;
    left: 180px;
    top: 318px;
    color: var(--paper);
    font-weight: 600;
    font-size: 29px;
    line-height: 34px;
    letter-spacing: 0.3px;
  }
</style>
</head>
<body>

<section class="postcard postcard--carpet">
  <svg class="postcard__art" viewBox="0 0 863 575" preserveAspectRatio="none">
    <defs>
      <linearGradient id="carpetTop" x1="0" y1="0" x2="1" y2="1">
        <stop offset="0" stop-color="#bdb7ae"/>
        <stop offset="0.6" stop-color="#8a847b"/>
        <stop offset="1" stop-color="#6b655d"/>
      </linearGradient>
      <linearGradient id="carpetMid" x1="0" y1="0" x2="1" y2="1">
        <stop offset="0" stop-color="#e4dccd"/>
        <stop offset="1" stop-color="#bdb3a4"/>
      </linearGradient>
      <linearGradient id="carpetSide" x1="0" y1="0" x2="0" y2="1">
        <stop offset="0" stop-color="#cfa078"/>
        <stop offset="0.5" stop-color="#e8e1d6"/>
        <stop offset="1" stop-color="#3a3a3a"/>
      </linearGradient>
    </defs>
    <polygon points="0,499 420,357 863,357 863,575 0,575" fill="var(--slate)"/>
    <polygon points="0,389 150,444 0,499" fill="var(--brand-blue)"/>
    <polygon points="0,110 340,110 358,145 0,145" fill="var(--brand-blue)"/>
    <polygon role="img" aria-label="Photo: vacuum cleaner on a shaggy carpet" points="223,0 863,0 863,222 645,305 560,250 455,145" fill="url(#carpetTop)"/>
    <polygon role="img" aria-label="Photo: vacuum cleaning a beige carpet" points="648,204 782,342 648,484 512,342" fill="url(#carpetMid)" stroke="#ffffff" stroke-width="9"/>
    <polygon role="img" aria-label="Photo: vacuum on a rug beside furniture" points="655,300 863,228 863,575 760,575 608,420" fill="url(#carpetSide)" stroke="#ffffff" stroke-width="9"/>
    <rect role="img" aria-label="Megaphone icon" x="188" y="410" width="80" height="82" rx="18" fill="#2b2b2b"/>
    <line x1="265" y1="434" x2="265" y2="549" stroke="var(--rule)" stroke-width="2"/>
    <circle cx="320" cy="464" r="32" fill="#ffffff"/>
    <path d="M302 470 q18 -22 36 0 l-4 4 h-28 z M308 474 h24 v10 h-24 z M302 466 v-6 q18 -12 36 0 v6 z" fill="var(--slate)"/>
  </svg>

  <div class="brand">
    <span class="brand__mark"></span>
    <span class="brand__rule"></span>
    <span class="brand__name">FIBER NEST</span>
  </div>
  <p class="audience">Commercial And Residential</p>
  <h2 class="headline"><span>Carpet</span><span class="accent">Cleaning</span><span>Services</span></h2>
  <p class="blurb">Lorem ipsum dolor sit amet, consectetuer adipiscing elit, sed diam nonummy nibh euismod tincidunt ut</p>
  <p class="hours">Call us on daily working<br>hours 00 am to 00 am</p>
  <p class="phone">555-319-4826</p>
</section>

<section class="postcard postcard--vent">
  <svg class="postcard__art" viewBox="0 0 863 575" preserveAspectRatio="none">
    <defs>
      <linearGradient id="ventTop" x1="0" y1="0" x2="1" y2="1">
        <stop offset="0" stop-color="#5a544a"/>
        <stop offset="0.5" stop-color="#d8d6d0"/>
        <stop offset="1" stop-color="#b89a6a"/>
      </linearGradient>
      <linearGradient id="ventMid" x1="0" y1="0" x2="1" y2="1">
        <stop offset="0" stop-color="#d6d6d6"/>
        <stop offset="1" stop-color="#6e6e6e"/>
      </linearGradient>
      <radialGradient id="ventSide" cx="0.6" cy="0.45" r="0.6">
        <stop offset="0" stop-color="#e9e9e9"/>
        <stop offset="0.7" stop-color="#8c8c8c"/>
        <stop offset="1" stop-color="#4a4a4a"/>
      </radialGradient>
    </defs>
    <polygon points="0,499 420,357 863,357 863,575 0,575" fill="var(--slate)"/>
    <polygon points="0,389 150,444 0,499" fill="var(--brand-blue)"/>
    <polygon points="0,110 340,110 358,145 0,145" fill="var(--brand-blue)"/>
    <polygon role="img" aria-label="Photo: technician servicing an outdoor unit" points="223,0 863,0 863,222 645,305 560,250 455,145" fill="url(#ventTop)"/>
    <polygon role="img" aria-label="Photo: foil dryer duct and round vent" points="648,204 782,342 648,484 512,342" fill="url(#ventMid)" stroke="#ffffff" stroke-width="9"/>
    <polygon role="img" aria-label="Photo: round ceiling air vent" points="655,300 863,228 863,575 760,575 608,420" fill="url(#ventSide)" stroke="#ffffff" stroke-width="9"/>
    <rect role="img" aria-label="Megaphone icon" x="188" y="410" width="80" height="82" rx="18" fill="#2b2b2b"/>
    <line x1="265" y1="434" x2="265" y2="549" stroke="var(--rule)" stroke-width="2"/>
    <circle cx="320" cy="464" r="32" fill="#ffffff"/>
    <path d="M302 470 q18 -22 36 0 l-4 4 h-28 z M308 474 h24 v10 h-24 z M302 466 v-6 q18 -12 36 0 v6 z" fill="var(--slate)"/>
  </svg>

  <div class="brand">
    <span class="brand__mark"></span>
    <span class="brand__rule"></span>
    <span class="brand__name">FIBER NEST</span>
  </div>
  <p class="audience">Commercial And Residential</p>
  <h2 class="headline"><span class="lead">Side Dryer Vent</span><span class="big accent">Cleaning</span><span class="big">Services</span></h2>
  <p class="blurb">Lorem ipsum dolor sit amet, consectetuer adipiscing elit, sed diam nonummy nibh euismod tincidunt ut</p>
  <p class="hours">Call us on daily working<br>hours 00 am to 00 am</p>
  <p class="phone">555-319-4826</p>
</section>

</body>
</html>
```